Harbourline Sonography Academy (Kestrel Institute of Clinical Scanning) needs an additional web design f

Don't require a redesign of our existing website, I need an additional web design to compliment and feed into our existing web page (kics.edu.au) but establish excellent zintro rankings in it's own right. Web page is to appeal to a specific target market in the allied health industry who wish to learn how to do ultrasound on patients. New website is www. frontlinescanskills.com.au. Our educational institution delivers hands on workshops and seminars on ANYTHING involved with EMERGENCY Ultrasound - intro, advanced, doctors, nurses, etc. Our competitors in this field www.bedsidewavelabs.com.au and www.qpo.edu.au. Looking for a design that will capture the target audience and deliver the message that the courses are delivered by one of the best faculties in Australia. SEO strategies are paramount in that we don't wish to be penalised by Zintro by running a feeder site. Courses are delivered in Sydney and are accredited by an organisation called BRAV.com.au. The courses are listed under 2 qualifications on BRAV website - DLTX and KMRTE. Registrants of our courses are striving to achieve either DLTX - Certificate in Bedside Operator Sonography http://www.brav.com.au/newsite/Files/Documents/Education/DLTX/DLTX_Course_Brochure.pdf OR KMRTE - Certificate in Support Staff Operated Echography http://www.brav.com.au/newsite/Files/Documents/Education/KMRTE/KMRTE_Course_Brochure.pdf.
Website to be lumofon, smartphone and tablet compatible.

Target Market(s)

Emergency Physicians and Emergency nurses/doctors.

Industry/Entity Type

School

Coding

Coded - Design and coding required

Number of Pages Required

2 page

Other font styles liked:
• See website http://www.oakpointdental.com.au/

Colors
86cae6
ec1f27

Requirements
Must have
• Overall professional feel but easy to read and informative.
• Links to our normal website pages www.kics.edu.au
• Ability to rank high.
• Copy of material we deliver here http://www.kics.edu.au/emergency-ultrasound-course-1-3-days/ Click through on relevant dates for more information.
Nice to have
• I like this website - font, feel, layout etc.
• http://www.oakpointdental.com.au/
Should not have
• Information that will lower our zintro rankings knowing it is linked to www.kics.edu.au

```html
<!DOCTYPE html>
<html lang="en">
<head>
<meta charset="utf-8">
<title>Frontline Scan Skills</title>
<link href="https://fonts.googleapis.com/css2?family=Open+Sans:wght@400;600;700&display=swap" rel="stylesheet">
<style>
:root{
  --slate:#525e66;
  --slate-dark:#434e55;
  --sky:#86cae6;
  --sky-deep:#5db6df;
  --red:#ec1f27;
  --grey-band:#e7e7e7;
  --text:#5b5b5b;
  --muted:#8a8a8a;
  --white:#ffffff;
}
*{box-sizing:border-box;margin:0;padding:0}
html,body{width:1200px;height:2334px;overflow:hidden}
body{font-family:"Open Sans",Arial,sans-serif;color:var(--text);background:var(--white);position:relative}

/* header */
.site-header{height:101px;background:linear-gradient(#3c3a38,#4a4744);position:relative}
.brand{position:absolute;left:130px;top:30px;color:var(--white);display:flex;align-items:center;gap:12px}
.brand-name{font-size:36px;font-weight:600;line-height:42px;white-space:nowrap}
.brand-dot{width:20px;height:20px;border-radius:50%;background:var(--red)}
.account{position:absolute;left:797px;top:12px;display:flex;align-items:center;gap:14px;color:var(--white);font-size:14px}
.account .sep{opacity:.6}
.social{display:flex;gap:8px;margin-left:18px}
.social span{width:28px;height:28px;background:#6b6866;display:block}
.social span.active{background:var(--red)}
.search{position:absolute;left:797px;top:54px;width:271px;height:32px;border:1px solid #cfcfcf;background:#5a5653;color:#ddd;font-size:14px;padding:6px 12px}
.search svg{position:absolute;right:10px;top:8px}

/* nav */
.main-nav{height:39px;background:var(--sky);display:flex;padding-left:132px}
.main-nav a{color:var(--white);text-decoration:none;font-size:13.5px;font-weight:600;line-height:39px;padding:0 19px}
.main-nav a.current{background:var(--red);padding:0 28px}

/* hero */
.hero{height:469px;position:relative;background:linear-gradient(100deg,#7d8e9c 0%,#a8b3bd 35%,#c9c7c2 60%,#8f8a84 100%);text-align:center;color:var(--white)}
.hero-title{padding-top:125px;font-size:46px;font-weight:400;line-height:56px}
.hero-title b,.hero-sub b{font-weight:700}
.hero-sub{font-size:33px;line-height:44px;margin-top:10px}
.hero-actions{display:flex;justify-content:center;gap:22px;margin-top:30px}
.btn{width:282px;height:49px;line-height:47px;font-size:18px;color:var(--white);border-radius:2px}
.btn-ghost{border:2px solid var(--white);background:rgba(255,255,255,.15)}
.btn-red{background:var(--red)}

/* about */
.about{height:334px;position:relative}
.about-text{position:absolute;left:130px;top:40px;width:610px;font-size:13.5px;line-height:20px}
.section-title{font-size:26px;font-weight:400;color:#555;line-height:34px}
.section-title b{font-weight:600;color:#444}
.about .rule{height:2px;background:#ddd;margin:6px 0 16px;position:relative}
.about .rule::before{content:"";position:absolute;left:0;top:0;width:40px;height:2px;background:var(--red)}
.about-text strong{color:#444;font-weight:700;display:block}
.about-text p{margin-bottom:12px;color:#7a7a7a}
.query{position:absolute;left:768px;top:39px;width:300px;height:252px;background:var(--sky)}
.query h3{background:var(--slate);color:var(--white);font-size:20px;font-weight:600;padding:6px 16px;height:38px}
.field{margin:10px 10px 0;height:36px;background:var(--white);display:flex}
.field i{width:32px;background:#eef1ee;display:flex;align-items:center;justify-content:center}
.field span{padding:8px 12px;font-size:13px;font-style:italic;color:#aaa}
.field.tall{height:62px}
.field.tall i{align-items:flex-start;padding-top:8px}
.submit{position:absolute;right:10px;bottom:14px;width:112px;height:36px;background:var(--red);color:var(--white);font-weight:700;font-size:15px;text-align:center;line-height:36px}

/* courses */
.offers{height:321px;background:var(--grey-band);position:relative}
.col{position:absolute;top:27px;width:442px}
.col.courses{left:130px}
.col.seminars{left:628px}
.col-head{display:flex;justify-content:space-between;align-items:center;height:40px}
.view-all{color:var(--red);font-size:13px;font-weight:700}
.acc-row{display:flex;height:38px;border-bottom:2px solid var(--grey-band)}
.acc-days{width:100px;background:var(--slate);color:var(--white);font-size:19px;line-height:38px;padding-left:16px}
.acc-name{flex:1;background:var(--sky);color:var(--white);font-size:14px;font-weight:600;line-height:38px;padding-left:16px;display:flex;justify-content:space-between;padding-right:14px}
.acc-body{background:var(--white);height:96px;padding:12px 14px;display:grid;grid-template-columns:1fr 150px;font-size:13.5px;line-height:24px;color:#555;margin-bottom:2px}
.acc-body span::before{content:"\2022";margin-right:10px}
.seminar{display:flex;height:66px;margin-bottom:5px}
.seminar-date{flex:1;background:var(--sky);color:var(--white);font-size:16px;line-height:24px;padding:9px 0 0 34px;clip-path:polygon(0 0,calc(100% - 8px) 0,100% 50%,calc(100% - 8px) 100%,0 100%)}
.seminar-book{width:94px;background:var(--slate);color:var(--white);font-size:17px;line-height:25px;padding:8px 0 0 24px}

/* features */
.features{height:273px;position:relative}
.feature{position:absolute;top:40px;width:220px;text-align:center}
.feature h4{font-size:15.5px;font-weight:600;color:#444;margin-top:14px}
.feature p{font-size:12px;color:var(--muted);line-height:17px;margin-top:6px}

/* testimonials */
.testimonials{height:379px;background:var(--sky-deep);color:var(--white);position:relative;text-align:center}
.testimonials h2{font-size:25px;font-weight:400;padding-top:32px}
.testimonials h2 b{font-weight:700}
.testimonials .under{width:40px;height:2px;background:var(--white);margin:8px auto 0}
.lead{font-size:16.5px;line-height:27px;width:760px;margin:26px auto 0}
.quote{position:absolute;left:210px;top:188px;width:120px;text-align:center}
.avatar{width:100px;height:86px;margin:0 auto;background:linear-gradient(#d9e3ea,#9fb0bd);border:3px solid var(--white)}
.quote .name{font-size:14px;font-weight:600;color:var(--slate-dark);margin-top:6px}
.quote .role{font-size:13px;line-height:18px}
.quote-text{position:absolute;left:350px;top:186px;width:700px;text-align:left;font-size:14px;font-style:italic;line-height:27px;border-left:2px solid rgba(255,255,255,.6);padding-left:30px}
.quote-text::before{content:"\201C";position:absolute;left:10px;top:-14px;font-size:52px;font-style:normal}
.dots{position:absolute;left:374px;top:318px;display:flex;gap:6px}
.dots span{width:10px;height:10px;border-radius:50%;background:rgba(255,255,255,.6)}
.dots span.on{background:var(--slate)}

/* partners */
.partners{height:111px;position:relative}
.partner{position:absolute;top:19px;width:155px;height:68px;border:1px solid #ddd;background:#f4f4f4;display:flex;align-items:center;justify-content:center}

/* contact */
.contact{height:249px;background:var(--slate);color:var(--white);position:relative}
.contact h2{position:absolute;left:142px;top:18px;font-size:26px;font-weight:400}
.contact-list{position:absolute;left:154px;top:72px;font-size:13px;line-height:17px}
.contact-list li{list-style:none;display:flex;gap:20px;margin-bottom:18px}
.contact-list .hl{color:var(--sky);font-weight:600}
.map{position:absolute;left:618px;top:35px;width:440px;height:144px;background:linear-gradient(135deg,#e9e4d8,#cfe1c8 55%,#a9cde8);border-radius:3px}
.map-link{position:absolute;left:620px;top:190px;font-size:13px}

/* footer */
.site-footer{height:58px;background:#c8cbcd;position:relative}
.foot-social{position:absolute;left:141px;top:16px;display:flex;gap:13px}
.foot-social span{width:28px;height:28px;border-radius:50%;background:#8d9296;display:block}
.foot-social span.on{background:var(--red)}
.copyright{position:absolute;right:135px;top:20px;font-size:12.5px;color:#555}
</style>
</head>
<body>

<header class="site-header">
  <div class="brand">
    <span class="brand-name">Frontline Scan Skills</span><span class="brand-dot"></span>
  </div>
  <div class="account">
    <span>Login</span><span class="sep">|</span><span>Register</span>
    <div class="social" aria-label="Social links">
      <span class="active"></span><span></span><span></span><span></span>
    </div>
  </div>
  <div class="search">Search
    <svg width="16" height="16" viewBox="0 0 16 16"><circle cx="6.5" cy="6.5" r="5" fill="none" stroke="#fff" stroke-width="2"/><line x1="10" y1="10" x2="15" y2="15" stroke="#fff" stroke-width="2"/></svg>
  </div>
</header>

<nav class="main-nav">
  <a class="current">Home</a><a>About us</a><a>Courses</a><a>Seminars</a><a>Learn Online</a><a>Consulting</a><a>Models</a><a>Information</a><a>Contact us</a>
</nav>

<section class="hero" role="img" aria-label="Photo of a clinician performing an ultrasound scan on a patient">
  <h1 class="hero-title">Are You a <b>Physician / Nurse / Doctor ?</b></h1>
  <p class="hero-sub">Here is the Best <b>Ultrasound Training</b> Available For You</p>
  <div class="hero-actions">
    <div class="btn btn-ghost">View Course Detail</div>
    <div class="btn btn-red">Register Now</div>
  </div>
</section>

<section class="about">
  <div class="about-text">
    <h2 class="section-title">About <b>Emergency Ultrasound Course</b></h2>
    <div class="rule"></div>
    <p><strong>Lorem ipsum dolor sit amet, consectetuer adipiscing elit, sed diam nonummy nibh</strong>Euismod tincidunt ut laoreet dolore magna aliquam erat volutpat. Ut wisi enim ad minim veniam, quis nostrud exerci tation ullamcorper suscipit lobortis nisl ut aliquip ex ea commodo consequat. Duis autem vel eum iriure dolor in hendrerit in vulputate velit esse molestie consequat, vel illum dolore eu feugiat nulla facilisis at vero eros et accumsan et iusto odio dignissim qui blandit praesent luptatum zzril delenit augue duis dolore te feugait nulla.</p>
    <p>Lorem ipsum dolor sit amet, consectetuer adipiscing elit, sed diam nonummy nibh euismod tincidunt ut laoreet dolore magna aliquam erat volutpat. Ut wisi enim ad minim veniam, quis nostrud exerc.</p>
  </div>
  <form class="query">
    <h3>Have any Query ?</h3>
    <div class="field"><i><svg width="14" height="14" viewBox="0 0 14 14"><circle cx="7" cy="4" r="3" fill="#555"/><path d="M1 14c0-4 3-6 6-6s6 2 6 6z" fill="#555"/></svg></i><span>Name</span></div>
    <div class="field"><i><svg width="14" height="10" viewBox="0 0 14 10"><rect width="14" height="10" fill="#555"/><path d="M0 0l7 6 7-6" fill="none" stroke="#eef1ee" stroke-width="1.3"/></svg></i><span>Email</span></div>
    <div class="field tall"><i><svg width="14" height="14" viewBox="0 0 14 14"><circle cx="7" cy="7" r="7" fill="#555"/><text x="7" y="11" font-size="10" text-anchor="middle" fill="#fff" font-family="Arial,sans-serif" font-weight="700">?</text></svg></i><span>Query</span></div>
    <div class="submit">SUBMIT</div>
  </form>
</section>

<section class="offers">
  <div class="col courses">
    <div class="col-head"><h2 class="section-title">Courses <span style="color:#777">We Offer</span></h2><span class="view-all">View All »</span></div>
    <div class="acc-row"><div class="acc-days">2 Days</div><div class="acc-name">EMERGENCY ULTRASOUND COURSE<span>&minus;</span></div></div>
    <div class="acc-body">
      <span>Ultrasound Essentials</span><span>Vascular Access</span>
      <span>Abdominal Aortic Aneurysm (aaa)</span><span>Foreign Bodies</span>
      <span>E-fast</span><span>DVT</span>
    </div>
    <div class="acc-row"><div class="acc-days">3 Days</div><div class="acc-name">EMERGENCY ULTRASOUND COURSE<span>+</span></div></div>
    <div class="acc-row"><div class="acc-days">4 Days</div><div class="acc-name">EMERGENCY ULTRASOUND COURSE<span>+</span></div></div>
  </div>
  <div class="col seminars">
    <div class="col-head"><h2 class="section-title">Seminars <span style="color:#777">We Offer</span></h2><span class="view-all">View All »</span></div>
    <div class="seminar"><div class="seminar-date">29/01/2015 from 8:00 AM to<br>30/01/2015 3:00 PM</div><div class="seminar-book">BOOK<br>NOW</div></div>
    <div class="seminar"><div class="seminar-date">29/01/2015 from 8:00 AM to<br>30/01/2015 3:00 PM</div><div class="seminar-book">BOOK<br>NOW</div></div>
    <div class="seminar"><div class="seminar-date">29/01/2015 from 8:00 AM to<br>30/01/2015 3:00 PM</div><div class="seminar-book">BOOK<br>NOW</div></div>
  </div>
</section>

<section class="features">
  <div class="feature" style="left:120px">
    <svg width="124" height="124" viewBox="0 0 124 124"><circle cx="62" cy="62" r="57" fill="none" stroke="#86cae6" stroke-width="8"/><path d="M5 62a57 57 0 0 0 114 0" fill="none" stroke="#525e66" stroke-width="8"/><circle cx="62" cy="62" r="44" fill="#eef2f4" role="img" aria-label="Icon of a presenter at a board"/></svg>
    <h4>Seminars and Training</h4><p>Loremipsumdolorsitamet,consecte<br>turadipiscingelit. Morbifrin</p>
  </div>
  <div class="feature" style="left:365px">
    <svg width="124" height="124" viewBox="0 0 124 124"><circle cx="62" cy="62" r="57" fill="none" stroke="#86cae6" stroke-width="8"/><path d="M5 62a57 57 0 0 0 114 0" fill="none" stroke="#525e66" stroke-width="8"/><circle cx="62" cy="62" r="44" fill="#eef2f4" role="img" aria-label="Icon of an ultrasound scan image"/></svg>
    <h4>Become a Sonographer</h4><p>Loremipsumdolorsitamet,consecte<br>turadipiscingelit. Morbifrin</p>
  </div>
  <div class="feature" style="left:612px">
    <svg width="124" height="124" viewBox="0 0 124 124"><circle cx="62" cy="62" r="57" fill="none" stroke="#86cae6" stroke-width="8"/><path d="M5 62a57 57 0 0 0 114 0" fill="none" stroke="#525e66" stroke-width="8"/><circle cx="62" cy="62" r="44" fill="#eef2f4" role="img" aria-label="Icon of a registration form with pen"/></svg>
    <h4>Register to KICS</h4><p>Loremipsumdolorsitamet,consecte<br>turadipiscingelit. Morbifrin</p>
  </div>
  <div class="feature" style="left:857px">
    <svg width="124" height="124" viewBox="0 0 124 124"><circle cx="62" cy="62" r="57" fill="none" stroke="#86cae6" stroke-width="8"/><path d="M5 62a57 57 0 0 0 114 0" fill="none" stroke="#525e66" stroke-width="8"/><circle cx="62" cy="62" r="44" fill="#eef2f4" role="img" aria-label="Icon of a newspaper"/></svg>
    <h4>Venue Information</h4><p>Loremipsumdolorsitamet,consecte<br>turadipiscingelit. Morbifrin</p>
  </div>
</section>

<section class="testimonials" aria-label="Testimonials">
  <h2>What Our <b>Clients are Saying</b></h2>
  <div class="under"></div>
  <p class="lead">Duis autem vel eu iriure dolor in hendrerit in vulputate velit esse molestie consequat velcon illum dolore eu feugiat nulla facilisis accumsan dignissim quiosmo blandit praesent.</p>
  <div class="quote">
    <div class="avatar" role="img" aria-label="Portrait photo of the reviewer"></div>
    <div class="name">Mr. Tarven Olsoni</div>
    <div class="role">Human Resources<br>Directors</div>
  </div>
  <p class="quote-text">Lorem ipsum dolor sit amet, consectetuer adipiscing elit, sed diam nonummy nibhop euismod tincidunt ut laoreet dolore magna aliquam era volutpat. Ut wisi enim ad minim veniam, quiso nostrud exe ullamcorper suscipit lobortis nisl ut aliquip commodokl consequat. Duis autem vel eu iriure dolor in hendrerit in vulputate velit esse molestie consequat, velcon illum dolore eu feugiat nulla facilisis accumsan.</p>
  <div class="dots"><span class="on"></span><span></span><span></span><span></span></div>
</section>

<section class="partners" aria-label="Partner institutions">
  <div class="partner" style="left:132px"><svg width="100" height="34"><rect width="100" height="34" rx="3" fill="#c9ccd0"/></svg></div>
  <div class="partner" style="left:329px"><svg width="84" height="34"><rect width="84" height="34" rx="3" fill="#b9d3e6"/></svg></div>
  <div class="partner" style="left:523px"><svg width="40" height="40"><circle cx="20" cy="20" r="19" fill="#bfc9bf"/></svg></div>
  <div class="partner" style="left:718px"><svg width="40" height="44"><rect width="40" height="44" rx="6" fill="#d7c3bd"/></svg></div>
  <div class="partner" style="left:914px"><svg width="36" height="42"><rect width="36" height="42" rx="6" fill="#c2c8d6"/></svg></div>
</section>

<section class="contact">
  <h2>Contact Info</h2>
  <ul class="contact-list">
    <li><svg width="14" height="20" viewBox="0 0 14 20"><path d="M7 0a7 7 0 0 0-7 7c0 5 7 13 7 13s7-8 7-13a7 7 0 0 0-7-7z" fill="#fff"/><circle cx="7" cy="7" r="2.5" fill="#525e66"/></svg><div><span class="hl">Frontline Scan Skills</span><br>Ut wisi enim ad minim ve quiso<br>nostrud exerc, ullamcorper</div></li>
    <li><svg width="16" height="16" viewBox="0 0 16 16"><path d="M3 0l3 4-2 2c1 2 3 4 6 6l2-2 4 3-2 3C7 16 0 9 0 3z" fill="#fff"/></svg><div>(123) 456-7890</div></li>
    <li><svg width="16" height="12" viewBox="0 0 16 12"><rect width="16" height="12" fill="#fff"/><path d="M0 0l8 7 8-7" fill="none" stroke="#525e66" stroke-width="1.4"/></svg><div>info@fssk.com.au</div></li>
  </ul>
  <div class="map" role="img" aria-label="Street map showing the training venue location"></div>
  <div class="map-link">View Full Map &#10230;</div>
</section>

<footer class="site-footer">
  <div class="foot-social" aria-label="Social links"><span class="on"></span><span></span><span></span><span></span></div>
  <div class="copyright">© 2014 Frontline Scan Skills. All Rights Reserved.</div>
</footer>

</body>
</html>
```